Business card for auto dealership

Looking for a clean modern design.
Would like attached logo incorporated

Industry/Entity Type

Car dealership

Contact Information for Business Card

Name, website, phone, cell, fax, email

```html
<!DOCTYPE html>
<html lang="en">
<head>
<meta charset="utf-8">
<title>Ridgeway Truck &amp; Auto Sales – Business Card</title>
<link rel="stylesheet" href="https://fonts.googleapis.com/css2?family=Roboto:wght@400;700&display=swap">
<style>
  :root {
    --backdrop: #2b2b2b;
    --ink: #000000;
    --paper: #ffffff;
    --card-shadow: rgba(0, 0, 0, 0.55);
  }
  * { box-sizing: border-box; margin: 0; padding: 0; }
  html, body {
    width: 1093px;
    height: 1200px;
    overflow: hidden;
    background: var(--backdrop);
    font-family: "Roboto", Arial, sans-serif;
  }
  .card {
    position: absolute;
    left: 264px;
    width: 580px;
    height: 358px;
    overflow: hidden;
    box-shadow: 3px 3px 6px var(--card-shadow);
  }
  .card--front { top: 226px; background: var(--paper); }
  .card--back  { top: 620px; background: var(--ink); }

  .front-wave {
    position: absolute;
    inset: 0;
    width: 100%;
    height: 100%;
  }

  .brand {
    position: absolute;
    font-weight: 700;
    line-height: 1;
    text-align: center;
  }
  .brand__name { display: block; letter-spacing: -0.5px; }
  .brand__tagline { display: block; letter-spacing: 0.5px; }

  .card--front .brand {
    right: 36px;
    top: 36px;
    color: var(--ink);
  }
  .card--front .brand__name { font-size: 50px; }
  .card--front .brand__tagline { font-size: 12px; margin-top: 4px; }

  .card--back .brand {
    left: 0;
    right: 0;
    top: 132px;
    color: var(--paper);
  }
  .card--back .brand__name { font-size: 64px; }
  .card--back .brand__tagline { font-size: 15px; margin-top: 6px; }

  .holder {
    position: absolute;
    left: 37px;
    top: 204px;
    color: var(--paper);
    font-size: 24px;
    font-weight: 400;
  }

  .contact {
    position: absolute;
    list-style: none;
    color: var(--paper);
    font-size: 16.5px;
  }
  .contact li {
    display: flex;
    align-items: center;
    height: 24.5px;
  }
  .contact--phones { left: 37px; top: 254px; }
  .contact--phones li { gap: 4px; }
  .contact--online { right: 34px; top: 279px; }
  .contact--online li { justify-content: flex-end; gap: 7px; }

  .icon {
    width: 20px;
    height: 20px;
    flex: none;
  }
</style>
</head>
<body>

<section class="card card--front" aria-label="Card front">
  <svg class="front-wave" viewBox="0 0 972 605" preserveAspectRatio="none" aria-hidden="true">
    <path fill="#000" d="M0,122 C330,290 650,385 850,385 C915,385 950,380 972,375 L972,605 L0,605 Z"/>
    <path fill="none" stroke="#fff" stroke-width="3" d="M0,145 C330,300 620,370 800,379"/>
  </svg>

  <div class="brand">
    <span class="brand__name">Ridgeway</span>
    <span class="brand__tagline">TRUCK &amp; AUTO SALES</span>
  </div>

  <p class="holder">Daniel Carver</p>

  <ul class="contact contact--phones">
    <li>
      <svg class="icon" viewBox="0 0 20 20" aria-label="Phone"><circle cx="10" cy="10" r="9" fill="none" stroke="#fff" stroke-width="1.2"/><path d="M6.5 5.5 L8.3 5.2 L9.2 7.6 L8 8.6 C8.6 10 9.8 11.3 11.3 12 L12.3 10.8 L14.6 11.7 L14.4 13.5 C10 13.8 6.2 10 6.5 5.5 Z" fill="none" stroke="#fff" stroke-width="1.1" stroke-linejoin="round"/></svg>
      <span>044-555 210 347</span>
    </li>
    <li>
      <svg class="icon" viewBox="0 0 20 20" aria-label="Mobile"><circle cx="10" cy="10" r="9" fill="none" stroke="#fff" stroke-width="1.2"/><rect x="7" y="5" width="6" height="10" rx="1" fill="none" stroke="#fff" stroke-width="1.1"/><circle cx="10" cy="13.3" r="0.7" fill="#fff"/></svg>
      <span>+91-555 318 620</span>
    </li>
    <li>
      <svg class="icon" viewBox="0 0 20 20" aria-label="Fax"><circle cx="10" cy="10" r="9" fill="#fff"/><rect x="7" y="5" width="6" height="3" fill="#000"/><rect x="5" y="8" width="10" height="5" rx="1" fill="#000"/><rect x="7" y="11" width="6" height="4" fill="#fff" stroke="#000" stroke-width="1"/></svg>
      <span>044-555 210 348</span>
    </li>
  </ul>

  <ul class="contact contact--online">
    <li>
      <span>hello@ridgewayauto.com</span>
      <svg class="icon" viewBox="0 0 20 20" aria-label="Email"><circle cx="10" cy="10" r="9" fill="none" stroke="#fff" stroke-width="1.2"/><rect x="5.5" y="6.5" width="9" height="7" fill="#fff"/><path d="M5.5 6.5 L10 10.5 L14.5 6.5" fill="none" stroke="#000" stroke-width="1"/></svg>
    </li>
    <li>
      <span>www.ridgewayauto.com</span>
      <svg class="icon" viewBox="0 0 20 20" aria-label="Website"><circle cx="10" cy="10" r="9" fill="none" stroke="#fff" stroke-width="1.2"/><circle cx="10" cy="10" r="5" fill="none" stroke="#fff" stroke-width="1"/><ellipse cx="10" cy="10" rx="2.2" ry="5" fill="none" stroke="#fff" stroke-width="1"/><path d="M5 10 H15 M5.7 7.5 H14.3 M5.7 12.5 H14.3" stroke="#fff" stroke-width="0.9"/></svg>
    </li>
  </ul>
</section>

<section class="card card--back" aria-label="Card back">
  <div class="brand">
    <span class="brand__name">Ridgeway</span>
    <span class="brand__tagline">TRUCK &amp; AUTO SALES</span>
  </div>
</section>

</body>
</html>
```